Redesign of Wine Label

A redesign of a French wine label (attached below - Images 1-3) that changes the following elements:
- Change out the ducks on a bicycle for a man on an old-fashioned bicycle (such as a penny-farthing bicycle) wearing the traditional hat of Gascogne, France (please see the following link - https://www.picsharely.com/domaine_morvenol/ - where you can find many examples of the red hat referenced)
- Please rearrange the words "Domaine Morvenol" so that the word "Morvenol" is larger, about double the size of the word "Domaine"
- Please include the words "Les Cousins" somewhere around "Domaine Morvenol" in a manner that shows the connection.
- Please include the words "Côtes de Gascogne" somewhere in smaller, though clearly visible, letters closer to the bottom of the label.
- Please make the bicycle like the old image attached, with two aristocratic men in the same type of clothing riding it.

```html
<!DOCTYPE html>
<html lang="fr">
<head>
<meta charset="utf-8">
<title>Domaine des cousins Morvenol – Malbec</title>
<link rel="stylesheet" href="https://fonts.googleapis.com/css2?family=Cormorant+Garamond:ital,wght@0,500;0,600;0,700;1,600;1,700&family=Cormorant+SC:wght@600;700&display=swap">
<style>
  :root {
    --page: #ededed;
    --paper: #fbfbfa;
    --plum: #3d1747;
    --plum-soft: #5a2d66;
    --gold: #b59a45;
    --gold-light: #f4e39a;
    --gold-deep: #c9a640;
  }
  html, body {
    margin: 0;
    width: 1200px;
    height: 1000px;
    overflow: hidden;
    background: var(--page);
  }
  .canvas {
    position: relative;
    width: 1200px;
    height: 1000px;
  }
  .label {
    position: absolute;
    left: 148px;
    top: 48px;
    width: 904px;
    height: 904px;
    background: linear-gradient(115deg, var(--gold-deep) 0%, var(--gold-light) 22%, var(--gold) 45%, var(--gold-light) 70%, var(--gold-deep) 100%);
  }
  .label__paper {
    position: absolute;
    inset: 35px;
    background: var(--paper);
  }
  .corner {
    position: absolute;
    width: 96px;
    height: 96px;
    border-radius: 12px;
    background: radial-gradient(circle, rgba(221,194,96,0.55), rgba(221,194,96,0.12) 70%, transparent);
  }
  .corner--tl { left: 38px; top: 22px; }
  .corner--tr { right: 38px; top: 22px; }
  .corner--bl { left: 38px; bottom: 22px; }
  .corner--br { right: 38px; bottom: 22px; }

  .title { position: absolute; left: 0; right: 0; top: 22px; height: 240px; color: var(--plum); font-family: "Cormorant Garamond", serif; }
  .title__domaine {
    position: absolute; left: 0; right: 0; top: 0;
    text-align: center; font-weight: 700; font-size: 54px; letter-spacing: 1px;
    padding-right: 40px;
  }
  .title__cousins {
    position: absolute; left: 500px; top: 70px;
    font-weight: 600; font-size: 34px;
  }
  .title__name {
    position: absolute; left: 0; right: 0; top: 80px;
    text-align: center; font-weight: 600; font-size: 150px; line-height: 1;
    padding-right: 20px;
  }
  .title__rule {
    position: absolute; top: 202px; height: 3px;
    border-top: 3px solid var(--plum); border-bottom: 3px solid var(--plum);
    padding-top: 6px;
  }
  .title__rule--left { left: 175px; width: 170px; }
  .title__rule--right { left: 480px; width: 200px; }

  .riders {
    position: absolute; left: 5px; top: 275px; width: 760px; height: 370px;
    background:
      radial-gradient(ellipse 22% 40% at 20% 68%, rgba(212,178,92,0.55), transparent 70%),
      radial-gradient(ellipse 22% 40% at 67% 68%, rgba(212,178,92,0.55), transparent 70%),
      radial-gradient(ellipse 12% 38% at 14% 30%, rgba(61,23,71,0.45), transparent 70%),
      radial-gradient(ellipse 12% 38% at 58% 30%, rgba(61,23,71,0.45), transparent 70%);
  }

  .details { position: absolute; left: 0; right: 0; top: 680px; text-align: center; }
  .details__grape {
    font-family: "Cormorant Garamond", serif; font-style: italic; font-weight: 700;
    font-size: 36px; color: var(--gold); line-height: 1;
  }
  .details__divider { display: block; margin: 8px auto 6px; }
  .details__region {
    font-family: "Cormorant SC", serif; font-weight: 700; font-size: 30px;
    color: var(--gold); letter-spacing: 1px; line-height: 1.1;
  }
  .details__legal {
    margin-top: 14px;
    font-family: "Cormorant SC", serif; font-weight: 700; font-size: 12.5px;
    color: var(--plum); letter-spacing: 0.3px;
  }
</style>
</head>
<body>
<div class="canvas">
  <div class="label">
    <div class="label__paper">
      <div class="corner corner--tl" role="img" aria-label="Gold flourish ornament"></div>
      <div class="corner corner--tr" role="img" aria-label="Gold flourish ornament"></div>
      <div class="corner corner--bl" role="img" aria-label="Gold flourish ornament"></div>
      <div class="corner corner--br" role="img" aria-label="Gold flourish ornament"></div>

      <header class="title">
        <div class="title__domaine">DOMAINE</div>
        <div class="title__cousins">des cousins</div>
        <div class="title__rule title__rule--left"></div>
        <div class="title__rule title__rule--right"></div>
        <div class="title__name">Morvenol</div>
      </header>

      <div class="riders" role="img" aria-label="Engraved illustration of two gentlemen in frock coats and caps riding penny-farthing bicycles with gold-tinted wheels"></div>

      <section class="details">
        <div class="details__grape">Malbec</div>
        <svg class="details__divider" width="190" height="12" viewBox="0 0 190 12" aria-hidden="true">
          <line x1="0" y1="6" x2="78" y2="6" stroke="#3d1747" stroke-width="2"/>
          <polygon points="84,6 89,1.5 94,6 89,10.5" fill="#3d1747"/>
          <polygon points="95,6 100,1.5 105,6 100,10.5" fill="#3d1747"/>
          <line x1="112" y1="6" x2="190" y2="6" stroke="#3d1747" stroke-width="2"/>
        </svg>
        <div class="details__region">Côtes de Gascogne</div>
        <div class="details__legal">Indication géographique protégée. Mis en bouteille à la propriété</div>
      </section>
    </div>
  </div>
</div>
</body>
</html>
```